IT Services company requires a services website design with integrated blog

We at Brindle Harbour Systems primarily provide application migration consultancy (e.g. moving applications from Plexor OS 4 to Plexor 9) and application virtualization (e.g. Norvane StackPod) consultancy.This process is commonly known as 'packaging' but doesnt involve cardboard boxes ;) (however, I am happy to use that visual analogy if you want to use any box graphics) We also provide application compatibility testing, software auditing and application portfolio management.

We are looking for a complete redesign of our current horrible diy attempt at a website at www.example-vendorhub.test. We have had created a rebranded logo (attached files and fonts) and a rebranded business card (also attached) We would like the website to match the same/similar colors and styling as these.

I want to redisgn the website so that the main focus of this website is to show our subject matter expertise with a blog and should take up most of the websites real estate and focus on the home screen. Then if the customer wants, they can use our services to help them in their own application migration/deployment projects by browsing our details in links/buttons somewhere
Updates

In any of the designs, please do not include my Quellbright or Norvane partnerships.  Thank you

Target Market(s)

Application packagers / engineers looking for technical articles

Application migration project managers

Industry/Entity Type

Real Estate

Requirements
Must have
• This site is primarily a blog site. The blog should have buttons to share each article on social media site. It should be easy for me to create or edit new blog articles (have technical skills but not creative ones). Each article should also allow for comments (do not require approval but should allow for admin removal) but do not add like/vote buttons because i do not expect large enough traffic and could be determental.

There should be a contact page to host contact information and an email box that goes to enquiries@example-vendorhub.test

The other pages should include About us and Services (placeholder text to be used as current site text needs overhauling but original text can be used in the design just remember when placing that the text may shorten or increase etc.)

All text has to be easily editable (no over use of text in images where possible)
Nice to have
• An email notification of new comments to articles sent to webadmin@example-vendorhub.test

Newsletter subscription
Should not have
• Do not include vote/like buttons or website counters. Initial traffic is not going to be large enough to warrant these features and may reflect badly on the site.

No logon features. Site content and commenting should be open access

No opinion polls

No why choose us section from current website

Do not include partner information in new site (Quellbright and Norvane)

DO NOT JUST REPLICATE EXISTING WEBSITE FEATURES, PLEASE REFER TO THIS BRIEF. THIS SITE NEEDS TO PRIMARILY BE A BLOG

```html
<!DOCTYPE html>
<html lang="en">
<head>
<meta charset="utf-8">
<title>Brindle Harbour Systems</title>
<link href="https://fonts.googleapis.com/css2?family=Jost:wght@400;500&display=swap" rel="stylesheet">
<style>
:root{
  --red:#e3001b;
  --dark:#2e2f2c;
  --darker:#1c1c1b;
  --black:#0a0a0a;
  --blue:#3a59c8;
  --link:#3b52b8;
  --grey-text:#8a8a8a;
  --body-text:#333;
  --line:#e2e2e2;
  --white:#fff;
}
*{box-sizing:border-box;margin:0;padding:0}
html,body{width:794px;height:1200px;overflow:hidden;background:var(--white)}
body{position:relative;font-family:"Jost",Arial,sans-serif;color:var(--body-text)}
.abs{position:absolute}

/* hero */
.hero{left:0;top:0;width:794px;height:382px;background:linear-gradient(90deg,#3a3a3a 0%,#6c6c6c 25%,#9a9a9a 45%,#b8b8b8 70%,#8e8e8e 100%)}
.hero-city{right:0;top:0;width:300px;height:382px;background:linear-gradient(180deg,#b5b5b5,#8a8a8a);opacity:.6}
.hero-text{left:353px;top:152px;width:345px;color:var(--white)}
.hero-text h1{font-weight:400;font-size:18px;line-height:24px}
.hero-text p{font-size:8.5px;line-height:12px;margin-top:10px}
.btn-blue{display:inline-block;background:var(--blue);color:var(--white);font-size:9.5px;padding:4px 30px;margin-top:14px}
.arrow{top:206px;width:22px;height:22px;border-radius:50%;background:#333}
.arrow svg{display:block}

/* header */
.header{left:90px;top:8px;width:598px;height:52px;background:var(--dark);border-right:4px solid var(--red)}
.logo{left:14px;top:12px;display:flex;align-items:center;gap:6px;color:#e8e8e8;font-size:11px}
.logo-dot{width:16px;height:16px;border-radius:50%;background:var(--blue)}
.nav{right:36px;top:26px;display:flex;gap:12px;font-size:8.5px;color:#ddd}
.nav .active{color:var(--red)}
.nav .sep{color:#888}
.searchbar{left:90px;top:60px;width:598px;height:21px;background:var(--darker);display:flex;align-items:center;padding-left:14px;font-size:7.5px;color:#ddd}
.searchbar .field{width:92px;height:12px;background:#111;border:1px solid #444;margin:0 3px}
.searchbar .go{background:var(--red);color:var(--white);padding:1px 9px;margin-right:6px}
.social{display:flex;gap:3px}
.social span{width:15px;height:13px;background:#555;display:block}
.searchbar .social{margin-left:auto;margin-right:22px}

/* about strip */
.tabs{left:0;top:382px;width:794px;height:32px;background:var(--black);color:var(--white);font-size:10px}
.tab{top:0;height:32px;line-height:38px}
.tab.on{left:103px;width:182px;background:var(--red);text-align:center}
.intro{left:0;top:414px;width:794px;height:135px;background:var(--red)}
.laptop{left:105px;top:20px;width:144px;height:96px;background:linear-gradient(180deg,#1b3b6f,#5aa3e0 60%,#333 62%,#1c1c1c)}
.intro-text{left:272px;top:17px;width:420px;color:var(--white);font-size:7.6px;line-height:11.5px}
.intro-text p+p{margin-top:3px}
.intro-text .btn-blue{font-size:7px;padding:3px 12px;margin-top:6px}

/* blog */
.section-title{font-size:10.5px;font-weight:400;color:#222;letter-spacing:.3px;padding-bottom:8px;border-bottom:1px solid var(--line)}
.blog{left:103px;top:572px;width:350px}
.post{margin-top:9px;padding-bottom:12px}
.post+.post{border-top:1px solid var(--line);padding-top:8px}
.post-head{display:flex;justify-content:space-between;align-items:center}
.post-title{color:var(--link);font-size:8.5px}
.tools{display:flex;gap:5px}
.tools span{width:8px;height:8px;border:1px solid #c66;display:block}
.date{display:inline-block;background:var(--black);color:var(--white);font-size:6.8px;padding:3px 6px;margin:10px 0 12px;border-bottom:2px solid #777}
.post p{font-size:6.8px;line-height:10px;color:var(--grey-text)}
.post p.code{color:#222;margin-top:6px}
.post p.lead-line{color:#222}
.post p.gap{margin-top:6px}
.post-foot{display:flex;justify-content:space-between;align-items:center;margin-top:12px}
.btn-red{background:var(--red);color:var(--white);font-size:7px;padding:3px 12px}
.share{display:flex;align-items:center;gap:5px;font-size:8px;color:#222}
.share span{display:block;width:30px;height:10px;border:1px solid #bbb;background:#f4f4f4}
.share span.sm{width:18px}

/* sidebar */
.sidebar{left:505px;top:572px;width:185px}
.sidebar .lead{font-size:6.8px;line-height:10px;color:#999;margin:6px 0 12px}
.services{border:1px solid var(--line)}
.services li{list-style:none;font-size:7.6px;padding:6px 9px;border-bottom:1px solid var(--line);background:linear-gradient(#fff,#f3f3f3)}
.news{margin-top:14px}
.news .tools{margin-top:10px}
.news-title{color:var(--link);font-size:8.5px;margin-top:10px}
.news small{display:block;font-size:6px;color:#888}
.news p{font-size:6.3px;line-height:9.5px;color:#666;margin-top:6px}

/* footer */
.footer{left:0;top:1015px;width:794px;height:151px;background:var(--dark);border-top:4px solid var(--red);color:#ddd}
.f-logo{left:103px;top:32px;display:flex;align-items:center;gap:7px;font-size:14px;color:#e8e8e8}
.f-logo .logo-dot{width:22px;height:22px}
.f-quote{left:103px;top:99px;width:165px;font-size:7.4px;line-height:10px;color:#999}
.f-quote em{display:block;text-align:right;font-style:normal;font-size:6.5px}
.f-col{top:33px;font-size:10px}
.f-col h3{font-weight:400;font-size:10px}
.news-col{left:318px;width:184px}
.news-col p{font-size:6.8px;line-height:10px;color:#888;margin:8px 0}
.subscribe{display:flex;gap:4px}
.subscribe .field{width:140px;height:17px;background:#111;font-size:6.5px;color:#888;padding:4px 5px}
.subscribe .btn-red{font-size:8px;padding:3px 6px}
.follow{display:flex;align-items:center;gap:14px;margin-top:12px;font-size:10px}
.contact-col{left:548px;width:150px}
.contact-col ul{list-style:none;margin-top:10px;font-size:6.5px;color:#999;line-height:9.5px}
.contact-col li{margin-bottom:5px}
.contact-col li.light{color:#ddd}
.contact-col strong{color:#ddd;font-weight:500}
.divider{top:30px;width:1px;height:100px;background:#444}
.copyright{left:0;top:1166px;width:794px;height:34px;background:var(--black);color:#ddd;font-size:7.5px;text-align:center;line-height:34px}
</style>
</head>
<body>

<div class="abs hero" role="img" aria-label="Photo of a businessman holding a glowing light in his open hand, city skyline behind"></div>
<div class="abs hero-city" role="img" aria-label="City skyline with tall tower"></div>
<div class="abs hero-text">
  <h1>We Have A Wide Range Of Experience In All Aspects Of Software Logistics</h1>
  <p>We can assist in managing your software from purchase to delivery and beyond for small and large enterprise projects, software vendors and cloud service operators.</p>
  <span class="btn-blue">Get Start Now !</span>
</div>
<div class="abs arrow" style="left:15px"><svg width="22" height="22"><path d="M13 7l-4 4 4 4" stroke="#fff" stroke-width="1.6" fill="none"/></svg></div>
<div class="abs arrow" style="left:755px"><svg width="22" height="22"><path d="M9 7l4 4-4 4" stroke="#fff" stroke-width="1.6" fill="none"/></svg></div>

<header class="abs header">
  <div class="abs logo"><span class="logo-dot"></span><span>Brindle Harbour Systems</span></div>
  <nav class="abs nav"><span class="active">Home</span><span class="sep">|</span><span>About Us</span><span class="sep">|</span><span>Our Services</span><span class="sep">|</span><span>Blog</span><span class="sep">|</span><span>Contact</span></nav>
</header>
<div class="abs searchbar">Search for :<span class="field"></span><span class="go">Search</span>Quick message widget for your users.<div class="social"><span></span><span></span><span></span><span></span><span></span></div></div>

<div class="abs tabs"><div class="abs tab on">About Us</div></div>
<section class="abs intro">
  <div class="abs laptop" role="img" aria-label="Laptop computer with blue abstract screen"></div>
  <div class="abs intro-text">
    <p>We have a wide range of experience in all aspects of software logistics. We can assist in managing your software from purchase to delivery and beyond for small and large enterprise projects, software vendors and cloud service operators.</p>
    <p>We know that your business is unique and that you need to react to market conditions quickly, therefore we tailor flexible services to your projects. We fully understand the complexities of managing your software and have proven methodologies to combat common problems.</p>
    <span class="btn-blue">Read More</span>
  </div>
</section>

<main class="abs blog">
  <h2 class="section-title">BLOG</h2>
  <article class="post">
    <div class="post-head"><span class="post-title">How To Run Local Applications Within a StackPod 5 Sequence</span><span class="tools"><span></span><span></span><span></span></span></div>
    <span class="date">Thursday, 08 November 2012 13:46</span>
    <p>Those of us that are used to StackPod before version 5 may be used to using the Podtray.exe with the /exe switch to run a command within the sequence. With StackPod 5 this has now gone. Instead StackPod 5 is ShellCore driven and there is a new cmdlet to achieve the same result. To do this you now run the following ShellCore cmdlets (this example executes editpad.exe within the My Application sequence):</p>
    <p class="code">Import-Module StackPodClient</p>
    <p class="code">$Package = Get-StackPodClientPackage ("My Application")</p>
    <p class="code">Start-StackPodVirtualProcess -StackPodClientObject $Package "editpad.exe"</p>
    <p class="gap">Note that Start-StackPodVirtualProcess accepts the same parameters as the standard Start-Process cmdlet such as the ability to change window style (such as minimized), run as a different user, etc.</p>
    <div class="post-foot"><span class="btn-red">Read More</span><div class="share">0 Comments <span></span><span></span><span class="sm"></span></div></div>
  </article>
  <article class="post">
    <div class="post-head"><span class="post-title">Isolating Vistaline Browser Within StackPod</span><span class="tools"><span></span><span></span><span></span></span></div>
    <span class="date">Thursday, 31 May 2012 10:25</span>
    <p class="lead-line">I recently came across a interesting scenario whilst sequencing Vistaline Browser add-ons.</p>
    <p class="gap">My scenario was this: I had an Vistaline based application that required a specific version of Korla. On the local PC image is a newer version of Korla. My sequence was to contain the specified version of Korla with a shortcut to the locally installed Vistaline Browser with the website as a parameter. In theory, when launching the website from my sequenced application shortcut the older version of Korla should be used and not the locally installed one.</p>
    <div class="post-foot"><span class="btn-red">Read More</span><div class="share">0 Comments <span></span><span></span><span class="sm"></span></div></div>
  </article>
</main>

<aside class="abs sidebar">
  <h2 class="section-title">OUR SERVICES</h2>
  <p class="lead">We offer the following services to our customers. Service levels are flexible; We can provide you with a dedicated expert/team, training of your own teams or simple consultation and health checks services. Please feel free to contact us to discuss your needs for a tailor made service package.</p>
  <ul class="services"><li>Initialisation</li><li>Portfolio Management</li><li>Packaging</li><li>Virtualization</li><li>Testing</li><li>Training and Consultancy</li><li>Build Management and Automation</li></ul>
  <div class="news">
    <h2 class="section-title">LATEST NEWS</h2>
    <div class="post-head"><span class="news-title">New Training Courses</span><span class="tools"><span></span><span></span><span></span></span></div>
    <small>Tuesday, 19 June 2012 16:47</small>
    <p>Brindle Harbour Systems are happy to announce new training courses for application packaging and testing teams</p>
  </div>
</aside>

<footer class="abs footer">
  <div class="abs f-logo"><span class="logo-dot"></span><span>Brindle Harbour Systems</span></div>
  <p class="abs f-quote">Logistics - The detailed organization and implementation of a complex operation<em>Larkfield Dictionary</em></p>
  <div class="abs divider" style="left:296px"></div>
  <div class="abs f-col news-col">
    <h3>Newsletter Subscribe</h3>
    <p>Stay up to date with latest news from our company. We promise we won't spam you.</p>
    <div class="subscribe"><span class="field">Enter your email here...</span><span class="btn-red">Sign Up</span></div>
    <div class="follow">Follow Us On :<div class="social"><span></span><span></span><span></span><span></span><span></span></div></div>
  </div>
  <div class="abs divider" style="left:528px"></div>
  <div class="abs f-col contact-col">
    <h3>Get In Touch</h3>
    <ul>
      <li><strong>Brindle Harbour Systems</strong><br>17 Fenwick Row Aldermoor<br>AB1 2CD United Kingdom</li>
      <li class="light">E-mail: enquiries@example-vendorhub.test</li>
      <li class="light">0800 000 0101<br>0800 000 0202</li>
    </ul>
  </div>
</footer>
<div class="abs copyright">Copyright © 2013 Brindle Harbour Systems Ltd. All Rights Reserved.</div>

</body>
</html>
```